Flyer-Design für Kurierdienst
Der gedruckte Flyer ist heute bei uns angekommen. Wir sind mit der Arbeit sehr zufrieden.
Zielgruppe
Wir sind ein Kurierdienst in Frankfurt am Main. Der Flyer soll auf unsere drei Kerndienstleistungen aufmerksam machen. Diese sind Direktfahrten innerhalb von Frankfurt, Deutschland und Europa, der nationale Versand über Nacht sowie der internationale Expressversand.
Unsere Zielgruppe sind ausschließlich Firmenkunden in Frankfurt. Vor allem möchten wir mit dem Flyer anspruchsvolle Kunden wie z.B. Anwaltskanzleien und Finanzdienstleister erreichen. Wir bieten einen Rundum-Service, geschulte Fahrer und feste Ansprechpartner (kein Callcenter).
Eine genauere Beschreibung unserer Dienstleistungen hängt an bzw. sind auf unserer Internetseite unter www.lindenhofmobil.com zu finden.
Aufgabenstellung
Wir haben uns einen zwei- oder vierseitigen DIN-Lang Flyer vorgestellt. Farblich sollte sich der Flyer am blau aus unserem Logo orientieren. Das angehangene "Die Lerche" Logo darf nur in Verbindung mit dem nationalen Versand über Nacht aufgeführt werden. Unsere Telefonnummer solle auf der Frontseite deutlich hervorgehoben sein.

```html
<!DOCTYPE html>
<html lang="de">
<head>
<meta charset="utf-8">
<title>Lindenhof Mobil – Flyer DIN lang</title>
<link rel="stylesheet" href="https://fonts.googleapis.com/css2?family=Ubuntu:wght@300;400;500;700&family=Tinos&display=swap">
<style>
  :root {
    --sky: #7fd8fc;
    --royal: #2069d3;
    --ink: #2262cc;
    --paper: #ffffff;
    --label: #111111;
  }
  * { margin: 0; padding: 0; box-sizing: border-box; }
  html, body { width: 1010px; height: 1200px; overflow: hidden; background: var(--paper); }
  body { position: relative; font-family: "Ubuntu", sans-serif; color: var(--ink); }

  .side-label {
    position: absolute; font-family: "Tinos", serif; font-size: 17px; color: var(--label);
    transform: translateX(-50%);
  }
  .side-label--front { left: 258px; top: 69px; }
  .side-label--back { left: 741px; top: 228px; }

  .flyer {
    position: absolute; width: 397px; height: 851px; background: var(--paper);
    box-shadow: 0 0 4px rgba(0,0,0,0.35); overflow: hidden;
  }
  .flyer--front { left: 73px; top: 109px; }
  .flyer--back { left: 542px; top: 267px; }
  .flyer__waves { position: absolute; inset: 0; width: 100%; height: 100%; }

  /* Vorderseite */
  .brand-name {
    position: absolute; top: 128px; left: 0; width: 100%; text-align: center;
    font-size: 27px; font-weight: 500; letter-spacing: 0.5px; color: var(--royal);
  }
  .band { position: absolute; left: 0; width: 100%; display: flex; align-items: center; justify-content: center; text-align: center; color: var(--paper); }
  .band--claim { top: 231px; height: 54px; background: var(--sky); font-size: 14.5px; font-weight: 300; line-height: 17px; }
  .band--promise { top: 551px; height: 44px; background: var(--royal); font-size: 14px; font-weight: 400; }
  .photo-area {
    position: absolute; top: 285px; left: 0; width: 100%; height: 266px;
    background: linear-gradient(115deg, #3b3f41 0%, #6c6b66 35%, #c9dfb6 65%, #e8efe3 100%);
  }
  .hotline {
    position: absolute; top: 707px; left: 0; width: 100%; text-align: center;
    font-size: 37px; font-weight: 700; color: var(--ink); letter-spacing: 0.5px;
  }
  .website {
    position: absolute; top: 747px; left: 0; width: 100%; text-align: center;
    font-size: 20px; font-weight: 700; color: var(--ink);
  }

  /* Rückseite */
  .service { position: absolute; left: 41px; width: 322px; }
  .service__title { font-size: 14px; font-weight: 700; line-height: 18px; margin-bottom: 5px; }
  .service__text { font-size: 12px; font-weight: 300; line-height: 17px; }
  .service--direct { top: 88px; }
  .service--overnight { top: 216px; }
  .service--international { top: 427px; }
  .service__text--dense { line-height: 16px; }
  .advice { position: absolute; left: 41px; top: 530px; width: 322px; font-size: 12px; font-weight: 300; line-height: 16px; }
  .advice strong { font-weight: 700; }

  .contact {
    position: absolute; top: 604px; left: 0; width: 100%; text-align: center;
    font-size: 12.5px; font-weight: 300; line-height: 15.8px;
  }
  .contact__name { font-weight: 700; }
  .contact__group { margin-bottom: 15.8px; }
</style>
</head>
<body>

<div class="side-label side-label--front">Vorderseite</div>
<div class="side-label side-label--back">Rückseite</div>

<section class="flyer flyer--front">
  <svg class="flyer__waves" viewBox="0 0 692 1482" preserveAspectRatio="none" aria-hidden="true">
    <path fill="var(--sky)" d="M0 0 H692 V135 C560 95 420 45 250 48 C130 50 40 75 0 90 Z"/>
    <path fill="var(--royal)" d="M0 1400 C120 1430 260 1432 400 1405 C520 1380 620 1345 692 1335 V1482 H0 Z"/>
  </svg>

  <div class="brand-name">LINDENHOF MOBIL</div>

  <div class="band band--claim">Ihre Sendung auf dem schnellsten Weg<br>zum Empfänger…</div>

  <div class="photo-area" role="img" aria-label="Foto: lächelnder Kurierfahrer am Steuer eines Transporters mit Klemmbrett und Paket"></div>

  <div class="band band--promise">… Ihr zuverlässiger Partner für dringende Transporte!</div>

  <div class="hotline">069-5550120-0</div>
  <div class="website">www.lindenhofmobil.com</div>
</section>

<section class="flyer flyer--back">
  <svg class="flyer__waves" viewBox="0 0 692 1482" preserveAspectRatio="none" aria-hidden="true">
    <path fill="var(--sky)" d="M0 0 H692 V130 C560 90 420 40 250 32 C140 28 50 45 0 62 Z"/>
    <path fill="var(--royal)" d="M0 1349 C150 1400 300 1440 450 1448 C560 1452 640 1440 692 1435 V1482 H0 Z"/>
  </svg>

  <article class="service service--direct">
    <h2 class="service__title">Direktfahrten</h2>
    <p class="service__text">Wir fahren jeden Tag für Sie, auch nachts und an Feiertagen. Deutschland- und Europaweit - vom Briefumschlag bis zur Europalette.</p>
  </article>

  <article class="service service--overnight">
    <h2 class="service__title">Nationaler Overnight-Versand</h2>
    <p class="service__text">Profitieren Sie als Lindenhof Mobil Kunde von unserer Anbindung an das leistungsstarke und NORMCERT zertifizierte (ISO 9001:2008) Netzwerk von Die Lerche.<br>Die Zustellung Ihrer Sendungen erfolgt am nächsten Werktag standardmäßig bis 12:00 Uhr (Inselzustellungen ausgenommen)<br>Selbstverständlich sind auch Frühtermine bis 10:00 Uhr, 09:00 Uhr oder 08:00 Uhr in viele Orte möglich.</p>
  </article>

  <article class="service service--international">
    <h2 class="service__title">Internationaler Versand</h2>
    <p class="service__text service__text--dense">Egal ob Terminzustellung am nächsten Werktag bis 12:00 in Paris, Madrid oder Los Angeles – wir sind Ihr Spezialist für eilige internationale Kuriersendungen.</p>
  </article>

  <p class="advice"><strong>Wir beraten Sie gerne</strong> bei der Wahl, der für Sie optimalen Liefervariante rund um die Welt.</p>

  <address class="contact" style="font-style: normal;">
    <div class="contact__group">
      <div class="contact__name">Lindenhof Mobil Frankfurt</div>
      <div>Jonas Weidner</div>
      <div>Birkenweg 12</div>
      <div>60599 Frankfurt am Main</div>
    </div>
    <div class="contact__group">
      <div>Tel: 069-5550120-0</div>
      <div>Fax: 069-55501299</div>
      <div>Mobil 069-55501288</div>
    </div>
    <div>
      <div>info@lindenhofmobil.com</div>
      <div>www.lindenhofmobil.com</div>
    </div>
  </address>
</section>

</body>
</html>
```